BrackenLeaf Billboards

We already hava a logo, slogan and general theme, we are looking for 2 to 3 billboard designs for out Recreational-Use Retail Cannabis Dispensary in NY state. We would like for the billboard to be a "Space" theme with a realistic-looking astronaut, we cannot have any "cartoon-like" images that would be attractive to children per state regulations. We would like the following wording included:
BrackenLeaf Cannabis Company - Oswego , slogan is "Products out of this world" , address of 287 Harlow Street - Oswego, Free Delivery - Orders over $150 . Our primary brand color is lime green.

```html
<!DOCTYPE html>
<html lang="en">
<head>
<meta charset="utf-8">
<title>BrackenLeaf Cannabis Company – Oswego Billboard</title>
<link href="https://fonts.googleapis.com/css2?family=Tinos:wght@400&family=Roboto+Condensed:ital,wght@1,800&display=swap" rel="stylesheet">
<style>
  :root {
    --space-deep: #04070f;
    --space-navy: #0b1a36;
    --earth-blue: #2f6fb8;
    --earth-glow: #7fb4ea;
    --white: #ffffff;
    --lime: #6cc644;
    --lime-light: #a4d94a;
    --lime-dark: #3f9a2c;
    --black: #050505;
  }
  * { margin: 0; padding: 0; box-sizing: border-box; }
  html, body { width: 1200px; height: 350px; overflow: hidden; background: var(--space-deep); }
  .billboard {
    position: relative;
    width: 1200px;
    height: 350px;
    overflow: hidden;
    font-family: "Tinos", "Times New Roman", serif;
    color: var(--white);
  }
  .space-scene {
    position: absolute; inset: 0;
    background:
      radial-gradient(ellipse 520px 300px at 1000px 470px, var(--earth-blue) 0%, #1d4d8c 55%, rgba(11,26,54,0) 80%),
      radial-gradient(circle 18px at 848px 100px, rgba(255,255,255,0.8), rgba(255,255,255,0) 100%),
      linear-gradient(100deg, var(--space-deep) 0%, var(--space-navy) 60%, #102a52 100%);
  }
  .astronaut-photo {
    position: absolute;
    left: 440px; top: 0;
    width: 400px; height: 350px;
    background: radial-gradient(ellipse 170px 175px at 200px 170px, #d9dde2 0%, #aeb4bc 55%, rgba(120,130,145,0) 100%);
  }
  .brand-block { position: absolute; left: 0; top: 0; width: 500px; text-align: center; }
  .brand-name {
    position: absolute; left: 42px; top: 72px; width: 410px;
    font-size: 62px; line-height: 1; font-variant: small-caps; letter-spacing: 0.5px;
  }
  .brand-sub {
    position: absolute; left: 42px; top: 131px; width: 410px;
    font-size: 35px; line-height: 1; text-transform: uppercase;
  }
  .brand-rule {
    position: absolute; left: 84px; top: 175px; width: 326px; height: 3px; background: var(--white);
  }
  .brand-city {
    position: absolute; left: 42px; top: 187px; width: 410px;
    font-size: 35px; line-height: 1; text-transform: uppercase;
  }
  .address {
    position: absolute; left: 55px; top: 266px;
    display: flex; align-items: center; gap: 8px;
    font-size: 28px; line-height: 1;
  }
  .address svg { width: 26px; height: 36px; }
  .slogan {
    position: absolute; left: 855px; top: 30px; width: 310px;
    text-align: center; line-height: 1; text-transform: uppercase;
  }
  .slogan-line { display: block; font-size: 48px; }
  .slogan-line--top { margin-left: -4px; }
  .slogan-line + .slogan-line { margin-top: 1px; }
  .slogan-world {
    display: block; font-size: 80px; margin-top: 0;
    background: linear-gradient(180deg, var(--lime-light) 0%, var(--lime) 50%, var(--lime-dark) 100%);
    -webkit-background-clip: text; background-clip: text; color: transparent;
  }
  .delivery { position: absolute; left: 860px; top: 215px; width: 330px; height: 125px; }
  .delivery svg { position: absolute; inset: 0; }
  .delivery-text {
    position: absolute; font-family: "Roboto Condensed", "Arial Narrow", sans-serif;
    font-style: italic; font-weight: 800; line-height: 1; text-transform: uppercase;
  }
  .delivery-free { left: 22px; top: 27px; font-size: 33px; color: var(--white); }
  .delivery-orders { left: 44px; top: 69px; font-size: 33px; color: var(--lime); }
  .delivery-price {
    left: 247px; top: 62px; width: 60px; text-align: center;
    font-size: 36px; color: var(--white); font-style: normal;
  }
  .delivery-price sup { font-size: 17px; vertical-align: 14px; }
</style>
</head>
<body>
<main class="billboard">
  <div class="space-scene" role="img" aria-label="Starry space backdrop with the curve of planet Earth glowing blue at the lower right"></div>
  <div class="astronaut-photo" role="img" aria-label="Realistic photograph of an astronaut in a white spacesuit floating in space"></div>

  <section class="brand-block">
    <h1 class="brand-name">BrackenLeaf</h1>
    <p class="brand-sub">Cannabis Company</p>
    <div class="brand-rule"></div>
    <p class="brand-city">Oswego</p>
  </section>

  <p class="address">
    <svg viewBox="0 0 26 36" aria-hidden="true">
      <ellipse cx="13" cy="31" rx="11" ry="4" fill="none" stroke="#6cc644" stroke-width="3"/>
      <path d="M13 1C6.4 1 2 5.8 2 11.6 2 19 13 30 13 30S24 19 24 11.6C24 5.8 19.6 1 13 1Z" fill="#6cc644"/>
      <circle cx="13" cy="11.5" r="4.5" fill="#04070f"/>
    </svg>
    287 Harlow Street - Oswego
  </p>

  <h2 class="slogan">
    <span class="slogan-line slogan-line--top">Products</span>
    <span class="slogan-line">Out of This</span>
    <span class="slogan-world">World</span>
  </h2>

  <div class="delivery">
    <svg viewBox="0 0 330 125" aria-hidden="true">
      <polygon points="30,65 57,3 57,65" fill="#050505"/>
      <polygon points="34,63 250,63 226,104 10,104" fill="#050505"/>
      <polygon points="12,20 218,20 206,62 0,62" fill="#6cc644"/>
      <polygon points="277,37 284,41 292,38 297,45 305,44 307,52 315,54 314,62 320,67 315,74 319,81 312,86 312,94 304,95 301,103 293,101 287,107 281,101 273,103 270,95 262,94 262,86 255,81 259,74 254,67 260,62 259,54 267,52 269,44 277,45" fill="#6cc644"/>
      <line x1="262" y1="52" x2="312" y2="52" stroke="#fff" stroke-width="1"/>
      <line x1="262" y1="96" x2="312" y2="96" stroke="#fff" stroke-width="1"/>
    </svg>
    <span class="delivery-text delivery-free">Free Delivery</span>
    <span class="delivery-text delivery-orders">Orders Over</span>
    <span class="delivery-text delivery-price"><sup>$</sup>150</span>
  </div>
</main>
</body>
</html>
```